Brivel Metrics New Website for Health Benefits Plan Decisioneering Tool Launch

Brivel Metrics is a SaaS provider of health benefits comparison tools. We need a new simple SaaS focused website to direct customers to our product

Target Market(s)

General Public comparing their health benefits plans from their employer or from the state exchanges in the US

Coding

Coded - Design and coding required

Number of Pages Required

3 page

Requirements
Must have
• Main page - "Know the Best Health Benefits Plan for You!"
Graphic of a person looking over papers on their desk
Compare Now button to link to SaaS product
About Us
Product Page

https://plovix.example/top-cloud-sites/

```html
<!DOCTYPE html>
<html lang="en">
<head>
<meta charset="utf-8">
<title>Brivel Metrics — Know the Best Health Benefits Plan for You</title>
<link rel="stylesheet" href="https://fonts.googleapis.com/css2?family=Cinzel:wght@400;500&family=Nunito:wght@400;600&display=swap">
<style>
  :root {
    --brand-blue: #29a8e0;
    --footer-blue: #2aaae2;
    --ink: #1c1c1c;
    --page-top: #ffffff;
    --page-bottom: #eef6fb;
    --scene-light: #e1f1f9;
    --scene-soft: #cfe7f4;
    --scene-slate: rgba(86, 116, 132, 0.42);
    --scene-navy: rgba(20, 40, 90, 0.30);
    --scene-warm: rgba(246, 120, 80, 0.18);
    --white: #ffffff;
  }
  * { margin: 0; padding: 0; box-sizing: border-box; }
  html, body { width: 1200px; height: 688px; overflow: hidden; }
  body {
    position: relative;
    font-family: "Nunito", sans-serif;
    background: linear-gradient(180deg, var(--page-top) 0%, var(--page-bottom) 100%);
  }
  .site-header {
    position: absolute; top: 0; left: 0; width: 1200px; height: 120px;
  }
  .brand {
    position: absolute; left: 162px; top: 40px;
    font-family: "Cinzel", serif; font-weight: 500;
    font-size: 30px; letter-spacing: 0.3px;
    color: var(--brand-blue); text-decoration: none;
  }
  .main-nav {
    position: absolute; top: 50px; left: 742px;
    display: flex; gap: 39px;
  }
  .main-nav a {
    font-size: 13.5px; color: var(--ink); text-decoration: none;
    text-transform: uppercase; letter-spacing: 0.2px;
  }
  .hero-copy {
    position: absolute; left: 164px; top: 270px;
  }
  .hero-title {
    font-family: "Cinzel", serif; font-weight: 500;
    font-size: 41px; line-height: 51px;
    color: var(--brand-blue); letter-spacing: 0;
  }
  .cta-button {
    position: absolute; left: 161px; top: 443px;
    width: 188px; height: 45px; border-radius: 23px;
    background: var(--brand-blue); color: var(--white);
    font-size: 15px; font-weight: 600; letter-spacing: 0.3px;
    display: flex; align-items: center; justify-content: center;
    text-decoration: none; text-transform: uppercase;
  }
  .hero-illustration {
    position: absolute; left: 589px; top: 142px;
    width: 540px; height: 496px; border-radius: 48px 0 0 0;
    background:
      radial-gradient(ellipse 38% 22% at 62% 30%, var(--scene-warm), transparent 70%),
      radial-gradient(ellipse 55% 40% at 52% 72%, var(--scene-navy), transparent 70%),
      radial-gradient(ellipse 70% 50% at 50% 62%, var(--scene-slate), transparent 75%),
      linear-gradient(135deg, var(--scene-light) 0%, var(--scene-soft) 60%, var(--page-bottom) 100%);
    -webkit-mask-image: linear-gradient(90deg, #000 80%, transparent 100%);
    mask-image: linear-gradient(90deg, #000 80%, transparent 100%);
  }
  .site-footer {
    position: absolute; left: 0; top: 643px; width: 1200px; height: 45px;
    background: var(--footer-blue);
    display: flex; align-items: center; justify-content: center;
    color: var(--white); font-size: 13.5px;
  }
</style>
</head>
<body>
  <header class="site-header">
    <a class="brand" href="#">Brivel Metrics</a>
    <nav class="main-nav">
      <a href="#">Home</a>
      <a href="#">About Us</a>
      <a href="#">Product Page</a>
    </nav>
  </header>

  <main>
    <section class="hero-copy">
      <h1 class="hero-title">Know the Best<br>Health Benefits<br>Plan for You!</h1>
    </section>
    <a class="cta-button" href="#">Compare Now</a>
    <div class="hero-illustration" role="img" aria-label="Illustration of a man at his office desk reviewing stacks of papers, with a wall clock, pinboard, plant and briefcase"></div>
  </main>

  <footer class="site-footer">
    <p>Copyright © 2020 BRIVEL METRICS. All Rights Reserved.</p>
  </footer>
</body>
</html>
```